ARC VOLLEY Business Card Project

I'd like to request a business card design for the new company I've launched.
The name of the company is "ARC VOLLEY" an indoor unmanned tennis practice facility.
We would like to see designs that use our brand identity color in the logo I've attached.
We hope to get the design with modern, luxurious and elegant tone and manner.
We hope the logo should not be too big.

Business card must have elements as below:
- Logo (One of the logos I've attached)
- Name (In Korean Text) : 박 서 윤
- Title (In Korean Text) : 대표
- Phone Number : 010-8472-3916
- Email Address : seoyun.park@arcvolley-example.co.kr
- Website : www.arcvolley-example.co.kr
- Instagram : arcvolley
- Address (In Korean text) : 경기도 용인시 수지구 풍덕천로 456 미래타워 5층 501호, 502호

Target Market(s)

Tennis amateurs in 20 to 40s

Industry/Entity Type

Sports, Hobby

Contact Information for Business Card

- Logo (One of the logos I've attached) - Name (In Korean Text) : 박 서 윤 - Title (In Korean Text) : 대표 - Phone Number : 010-8472-3916 - Email Address : seoyun.park@arcvolley-example.co.kr - Website : www.arcvolley-example.co.kr - Instagram : arcvolley - Address (In Korean text) : 경기도 용인시 수지구 풍덕천로 456 미래타워 5층 501호, 502호

Font styles to use
Sans Serif

Requirements
Must have
• Double sided
Nice to have
• Logo with intaglio or relief embossing
Should not have
• Logo should not be too big.

```html
<!DOCTYPE html>
<html lang="ko">
<head>
<meta charset="utf-8">
<title>ARC VOLLEY Business Card</title>
<link href="https://fonts.googleapis.com/css2?family=Barlow+Semi+Condensed:wght@400;500&family=Noto+Sans+KR:wght@400&family=Noto+Serif+KR:wght@500&display=swap" rel="stylesheet">
<style>
  :root {
    --backdrop: #959595;
    --brand-green: #2d5a37;
    --brand-green-deep: #274f30;
    --emboss-line: #3a6a44;
    --card-paper: #efefef;
    --ink-green: #2f5a3a;
    --logo-grey: #9a9a9a;
  }
  * { margin: 0; padding: 0; box-sizing: border-box; }
  html, body { width: 1200px; height: 1000px; overflow: hidden; }
  body {
    background: var(--backdrop);
    position: relative;
    font-family: "Barlow Semi Condensed", "Noto Sans KR", sans-serif;
  }
  .card {
    position: absolute;
    left: 291px;
    width: 615px;
    height: 351px;
    border-radius: 30px;
    overflow: hidden;
  }
  .card-front { top: 116px; background: var(--brand-green); }
  .card-back { top: 524px; background: var(--card-paper); }

  .front-mark { position: absolute; left: 750px; top: 330px; }

  .brand {
    position: absolute;
    left: 42px;
    top: 32px;
    display: flex;
    align-items: center;
    gap: 12px;
  }
  .brand-name {
    font-family: "Barlow Semi Condensed", sans-serif;
    font-weight: 400;
    font-size: 27px;
    letter-spacing: 1px;
    color: var(--logo-grey);
  }

  .person {
    position: absolute;
    left: 41px;
    top: 124px;
    font-family: "Noto Serif KR", serif;
    font-weight: 500;
    font-size: 36px;
    line-height: 46px;
    color: var(--ink-green);
  }
  .rule {
    position: absolute;
    left: 41px;
    right: 36px;
    top: 232px;
    height: 1px;
    background: var(--ink-green);
  }
  .contact {
    position: absolute;
    list-style: none;
    color: var(--ink-green);
    font-size: 17px;
    letter-spacing: 0.2px;
  }
  .contact li {
    display: flex;
    align-items: center;
    gap: 10px;
    height: 28px;
    white-space: nowrap;
  }
  .contact svg { flex: none; }
  .contact-main { left: 41px; top: 242px; }
  .contact-web { right: 40px; top: 242px; }
  .contact .address {
    font-family: "Noto Sans KR", sans-serif;
    font-size: 14px;
    letter-spacing: 0;
  }
</style>
</head>
<body>

<section class="card card-front" aria-label="Business card front">
</section>
<svg class="front-mark" width="96" height="96" viewBox="0 0 96 96" aria-hidden="true">
  <circle cx="46" cy="47" r="42" fill="none" stroke="var(--emboss-line)" stroke-width="3"/>
  <circle cx="46" cy="47" r="42" fill="none" stroke="var(--brand-green-deep)" stroke-width="1" transform="translate(1 1.5)"/>
</svg>

<section class="card card-back" aria-label="Business card back">
  <div class="brand">
    <svg width="48" height="48" viewBox="0 0 48 48" aria-hidden="true">
      <circle cx="24" cy="24" r="22" fill="none" stroke="var(--logo-grey)" stroke-width="1.6"/>
    </svg>
    <span class="brand-name">ARC VOLLEY</span>
  </div>

  <h1 class="person">박 서 윤<br>대표</h1>

  <div class="rule"></div>

  <ul class="contact contact-main">
    <li>
      <svg width="15" height="15" viewBox="0 0 24 24" aria-hidden="true"><path fill="var(--ink-green)" d="M6.6 10.8a15.1 15.1 0 0 0 6.6 6.6l2.2-2.2c.3-.3.7-.4 1-.2 1.1.4 2.3.6 3.6.6.6 0 1 .4 1 1V20c0 .6-.4 1-1 1A17 17 0 0 1 3 4c0-.6.4-1 1-1h3.5c.6 0 1 .4 1 1 0 1.3.2 2.5.6 3.6.1.3 0 .7-.2 1z"/></svg>
      <span>010-8472-3916</span>
    </li>
    <li>
      <svg width="15" height="15" viewBox="0 0 24 24" aria-hidden="true"><path fill="var(--ink-green)" d="M2 5h20v14H2z"/><path fill="none" stroke="var(--card-paper)" stroke-width="1.6" d="M2.5 5.5 12 13l9.5-7.5M2.5 18.5l7-6.5m12 6.5-7-6.5"/></svg>
      <span>seoyun.park@arcvolley-example.co.kr</span>
    </li>
    <li>
      <svg width="15" height="15" viewBox="0 0 24 24" aria-hidden="true"><path fill="var(--ink-green)" d="M12 2a7 7 0 0 0-7 7c0 5 7 13 7 13s7-8 7-13a7 7 0 0 0-7-7zm0 9.5A2.5 2.5 0 1 1 12 6.5a2.5 2.5 0 0 1 0 5z"/></svg>
      <span class="address">경기도 용인시 수지구 풍덕천로 456 미래타워 5층 501호, 502호</span>
    </li>
  </ul>

  <ul class="contact contact-web">
    <li>
      <svg width="15" height="15" viewBox="0 0 24 24" aria-hidden="true"><g fill="none" stroke="var(--ink-green)" stroke-width="2"><circle cx="12" cy="12" r="10"/><ellipse cx="12" cy="12" rx="4.5" ry="10"/><path d="M2 12h20M4 7h16M4 17h16"/></g></svg>
      <span>arcvolley-example.co.kr</span>
    </li>
    <li>
      <svg width="15" height="15" viewBox="0 0 24 24" aria-hidden="true"><circle cx="12" cy="12" r="9.5" fill="none" stroke="var(--ink-green)" stroke-width="2.2"/></svg>
      <span>arcvolley</span>
    </li>
  </ul>
</section>

</body>
</html>
```